Business cards Marta Kessel Sport & Events

I need new business cards to match my new logo design for my company called "Marta Kessel Sport & Events". I'm based in Germany.
With my company, I offer different services in the context of sport.

Marta Kessel owner

Marta Kessel Sports & Events
Birkenfelder Weg 12
D-63118 Offenbach

+49 69 / 31 52 94 07
info@marta-kessel.example
www.marta-kessel.example

Contact Information for Business Card

Marta Kessel Inhaberin Marta Kessel Sport & Events Birkenfelder Weg 12 D-63118 Offenbach +49 69 / 31 52 94 07 info@marta-kessel.example www.marta-kessel.example

Requirements
Must have
• Logo | Double sided business card

```html
<!DOCTYPE html>
<html lang="de">
<head>
<meta charset="utf-8">
<title>Marta Kessel Sport &amp; Events – Visitenkarten</title>
<link rel="stylesheet" href="https://fonts.googleapis.com/css2?family=Arimo:wght@400;700&display=swap">
<style>
  :root {
    --page-bg: #e6e6e4;
    --card-white: #fbfbfa;
    --card-dark: #2a2a2d;
    --brand-orange: #f29d1e;
    --edge-orange: #c98a12;
    --ink: #1b1b1b;
    --logo-grey: #5b5c60;
  }
  * { margin: 0; padding: 0; box-sizing: border-box; }
  html, body {
    width: 1200px; height: 801px; overflow: hidden;
    background: var(--page-bg);
    font-family: "Arimo", Arial, sans-serif;
    color: var(--ink);
  }
  .sheet {
    width: 1200px; height: 801px;
    display: flex; align-items: center; justify-content: center; gap: 30px;
  }
  .card {
    position: relative;
    width: 560px; height: 320px;
    border-bottom: 3px solid var(--edge-orange);
    box-shadow: 0 10px 24px rgba(0,0,0,.18);
  }
  .card--front { background: var(--card-white); }
  .card--back { background: var(--card-dark); display: flex; align-items: center; justify-content: center; }

  .brand { display: flex; align-items: center; gap: 12px; }
  .brand__dot { width: 52px; height: 52px; border-radius: 50%; background: var(--brand-orange); flex: none; }
  .brand__name { font-weight: 700; text-transform: uppercase; line-height: 1.05; letter-spacing: .06em; }
  .brand__name small { display: block; font-size: .55em; letter-spacing: .3em; }

  .card--front .brand { position: absolute; top: 34px; left: 190px; }
  .card--front .brand__name { color: var(--ink); font-size: 22px; }

  .card--back .brand { gap: 18px; }
  .card--back .brand__dot { width: 96px; height: 96px; }
  .card--back .brand__name { color: var(--brand-orange); font-size: 34px; }

  .holder { position: absolute; left: 44px; top: 150px; }
  .holder__name { color: var(--brand-orange); font-size: 24px; font-weight: 700; text-transform: uppercase; letter-spacing: .01em; }
  .holder__role { font-size: 15px; margin-top: 2px; }

  .divider { position: absolute; left: 44px; right: 30px; top: 206px; height: 1px; background: var(--ink); }

  .contacts { position: absolute; left: 44px; top: 220px; list-style: none; font-size: 14.5px; }
  .contacts li { display: flex; align-items: center; gap: 12px; height: 24px; }
  .contacts svg { width: 16px; height: 16px; fill: var(--brand-orange); flex: none; }

  .address { position: absolute; right: 30px; top: 220px; text-align: right; font-size: 14.5px; font-style: normal; line-height: 24px; }
</style>
</head>
<body>
<main class="sheet">
  <section class="card card--front" aria-label="Vorderseite">
    <div class="brand">
      <span class="brand__dot"></span>
      <span class="brand__name">Marta Kessel<small>Sport &amp; Events</small></span>
    </div>

    <div class="holder">
      <p class="holder__name">Marta Kessel</p>
      <p class="holder__role">Inhaberin</p>
    </div>

    <div class="divider"></div>

    <ul class="contacts">
      <li>
        <svg viewBox="0 0 16 16" aria-hidden="true"><path d="M3.5 1.5l2.5 0 1 3.5-1.8 1.2a8 8 0 0 0 4.6 4.6L11 9l3.5 1v2.5c0 1-1 2-2 2A11 11 0 0 1 1.5 3.5c0-1 1-2 2-2z"/></svg>
        +49 69 / 31 52 94 07
      </li>
      <li>
        <svg viewBox="0 0 16 16" aria-hidden="true"><path d="M1 3h14v10H1z M1 3l7 6 7-6" stroke="#fbfbfa" stroke-width="1.2"/></svg>
        info@marta-kessel.example
      </li>
      <li>
        <svg viewBox="0 0 16 16" aria-hidden="true"><circle cx="8" cy="8" r="7"/><path d="M1 8h14M8 1c-3 3-3 11 0 14M8 1c3 3 3 11 0 14" stroke="#fbfbfa" stroke-width="1.1" fill="none"/></svg>
        www.marta-kessel.example
      </li>
    </ul>

    <address class="address">
      Birkenfelder<br>
      Weg 12<br>
      D-63118 Offenbach
    </address>
  </section>

  <section class="card card--back" aria-label="Rückseite">
    <div class="brand">
      <span class="brand__dot"></span>
      <span class="brand__name">Marta Kessel<small>Sport &amp; Events</small></span>
    </div>
  </section>
</main>
</body>
</html>
```